New Pain Management Physcian Private Practice webpage design

Interventional Pain Management Company looking for new website. Want it modeled very closely to http://www.brivoltclinic.example/ website. Under navigation panel at top of main webpage take off the following tabs: About, Locations, News, Testimonial, and Pain Channel. Add New Patient visit tab, change about to Main Page, change treatments to Procedures, change Providers to Provider.Main web page should have the KTR logo, no picture slideshow for now but want ability to add pictures to the slideshow in the future. Pictures are included to show you an idea of what main page should look like. Colors are teal,Deep Navy, and White as shown in KTR logo. Font style should also be same as KTR logo.

Target Market(s)

Patients with all kinda of acute and chronic pain. Especially neck, mid back,low back pain, and joint pain.

Industry/Entity Type

Medical

Coding

Number of Pages Required

5+ page

Requirements
Must have
• See Project description above
Nice to have
• ability to add pictures to the slideshow in future
Should not have
• not applicable

```html
<!DOCTYPE html>
<html lang="en">
<head>
<meta charset="utf-8">
<title>Kovar Total Relief – Home</title>
<link href="https://fonts.googleapis.com/css2?family=Open+Sans:ital,wght@0,400;0,600;0,700;1,400;1,600&display=swap" rel="stylesheet">
<style>
:root{
  --teal:#1f8f9c;
  --teal-light:#4fb3bd;
  --navy:#1c2a3a;
  --navy-deep:#131d29;
  --ink:#3a3f45;
  --muted:#7a8088;
  --line:#e2e5e8;
  --paper:#ffffff;
  --mist:#f3f4f5;
}
*{box-sizing:border-box;margin:0;padding:0}
html,body{width:841px;height:1200px;overflow:hidden;background:var(--paper)}
body{font-family:"Open Sans",Arial,sans-serif;color:var(--ink);position:relative;font-size:10px}
.abs{position:absolute}

/* top bar */
.topbar{left:0;top:0;width:841px;height:38px;background:var(--mist);border-bottom:1px solid var(--line)}
.topbar .contact{left:200px;top:12px;font-size:9px;color:var(--muted);display:flex;gap:22px}
.topbar .contact span{display:flex;align-items:center;gap:5px}
.book-btn{left:650px;top:0;width:160px;height:32px;background:var(--teal);color:#fff;font-size:11px;font-weight:600;display:flex;align-items:center;justify-content:center;border-radius:0 0 4px 4px}

/* header */
.brand{left:28px;top:40px;display:flex;align-items:center;gap:8px}
.brand-mark{width:26px;height:26px;background:var(--teal);border-radius:3px}
.brand-name{font-size:15px;font-weight:700;color:var(--navy);letter-spacing:.5px}
.nav{left:230px;top:52px;display:flex;gap:20px;font-size:10.5px;color:var(--ink)}
.nav a{color:inherit;text-decoration:none}
.nav .active{color:var(--teal);font-weight:600}

/* hero */
.hero{left:0;top:80px;width:841px;height:245px;background:linear-gradient(90deg,#d8d6d2 0%,#eceae6 45%,#e9e9e8 100%)}
.hero-photo{left:90px;top:80px;width:340px;height:245px;background:linear-gradient(135deg,#cfc9c2,#b9b4ad 60%,#d9d4ce)}
.hero-title{left:470px;top:110px;width:330px;font-size:24px;line-height:30px;font-style:italic;color:var(--navy);text-align:right}
.hero-btn{left:690px;top:203px;width:100px;height:26px;background:var(--teal);color:#fff;font-size:10.5px;display:flex;align-items:center;justify-content:center;border-radius:2px}
.hero-arrow{top:190px;width:20px;height:34px;background:rgba(28,42,58,.55);display:flex;align-items:center;justify-content:center}

/* service cards */
.card{top:305px;width:152px;height:115px;background:#fff;border:1px solid var(--line);box-shadow:0 2px 4px rgba(0,0,0,.08);text-align:center;padding-top:40px}
.card-icon{left:50%;top:-18px;width:52px;height:52px;margin-left:-26px;border-radius:50%;background:var(--navy);border:3px solid #fff}
.card h3{font-size:12px;font-style:italic;font-weight:600;color:var(--navy);margin-bottom:6px}
.card p{font-size:8px;line-height:11px;color:var(--muted);padding:0 14px}
.card .bar{position:absolute;left:0;bottom:0;width:100%;height:4px;background:var(--teal)}

/* schedule form */
.schedule{left:546px;top:315px;width:265px;height:345px;background:#fff;border:1px solid var(--line);box-shadow:0 2px 6px rgba(0,0,0,.1)}
.schedule-head{height:34px;background:var(--navy);color:#fff;font-size:12px;font-weight:600;padding:10px 14px}
.schedule-intro{font-size:11px;color:var(--navy);padding:10px 14px 8px;line-height:15px}
.field{margin:0 14px 8px;height:22px;border:1px solid var(--line);font-size:8.5px;color:var(--muted);padding:5px 7px}
.field.msg{height:50px}
.captcha-note{font-size:8px;color:var(--muted);margin:8px 14px 5px}
.captcha-row{display:flex;gap:8px;align-items:center;margin:0 14px}
.captcha-code{width:46px;height:22px;background:var(--mist);border:1px solid var(--line);font-size:10px;font-weight:700;color:var(--navy);display:flex;align-items:center;justify-content:center}
.captcha-input{width:46px;height:22px;border:1px solid var(--line)}
.submit{width:60px;height:24px;background:var(--teal);color:#fff;font-size:9.5px;font-weight:600;display:flex;align-items:center;justify-content:center;margin-left:auto;border-radius:2px}

/* welcome */
.welcome{left:30px;top:505px;width:390px}
.welcome h2{font-size:13px;font-weight:600;color:var(--navy);margin-bottom:8px}
.welcome h2 em{color:var(--teal);font-style:normal}
.welcome p{font-size:8.5px;line-height:13px;color:var(--muted)}
.welcome .more{display:inline-block;margin-top:8px;font-size:9.5px;font-weight:600;color:var(--navy)}
.doctor-photo{left:432px;top:540px;width:92px;height:100px;background:linear-gradient(180deg,#c8b9a8,#6b6f77 70%,#3e4550)}
.doctor-name{left:420px;top:648px;width:116px;text-align:center;font-size:9px;color:var(--ink)}

.rule{left:30px;top:705px;width:781px;height:1px;background:var(--line)}

/* info columns */
.col{top:722px}
.col h4{font-size:12.5px;font-style:italic;font-weight:600;color:var(--teal);margin-bottom:10px}
.col h4 b{color:var(--navy);font-weight:600}
.list{list-style:none;font-size:9px;color:var(--ink)}
.list li{display:flex;align-items:center;gap:6px;height:17px}
.list li::before{content:"";width:0;height:0;border-left:4px solid var(--teal);border-top:3px solid transparent;border-bottom:3px solid transparent}
.insurance p{font-size:9.5px;line-height:15px;color:var(--ink)}
.insurance .more{display:block;margin-top:6px;font-size:9.5px;color:var(--teal)}
.causes{display:flex;gap:22px}

/* footer */
.footer{left:0;top:950px;width:841px;height:210px;background:var(--navy)}
.fcol{top:968px;color:#c7cdd4}
.fcol h5{font-size:12.5px;font-style:italic;font-weight:600;color:#fff;margin-bottom:10px}
.flinks{list-style:none;font-size:8.5px}
.flinks li{height:14px;display:flex;align-items:center;gap:6px}
.flinks li::before{content:"";width:3px;height:3px;background:var(--teal-light)}
.hours p{font-size:8.5px;line-height:13px}
.hours b{color:#fff;font-weight:600}
.news p{font-size:8.5px;line-height:13px;margin-bottom:8px}
.news .input{width:150px;height:20px;background:#fff;font-size:8px;color:var(--muted);padding:4px 7px;margin-bottom:6px}
.news .go{width:60px;height:20px;background:var(--teal);color:#fff;font-size:8.5px;display:flex;align-items:center;justify-content:center}
.fbrand{left:690px;top:1010px;display:flex;align-items:center;gap:7px}
.fbrand .brand-mark{width:22px;height:22px}
.fbrand .brand-name{color:#fff;font-size:12px}
.copyright{left:0;top:1160px;width:841px;height:40px;background:var(--navy-deep);color:#98a1ab;font-size:8.5px;display:flex;align-items:center;justify-content:center}
</style>
</head>
<body>

<!-- top bar -->
<div class="abs topbar">
  <div class="abs contact">
    <span><svg width="10" height="8" viewBox="0 0 10 8"><rect x=".5" y=".5" width="9" height="7" fill="none" stroke="#7a8088"/><path d="M.5 .5 5 4.5 9.5 .5" fill="none" stroke="#7a8088"/></svg>info@kovartotalrelief.example</span>
    <span><svg width="9" height="9" viewBox="0 0 9 9"><path d="M2 .5 3.5 2.5 2.5 3.5Q3.5 5.5 5.5 6.5L6.5 5.5 8.5 7 7.5 8.5Q1 7.5 .5 1.5Z" fill="#7a8088"/></svg>(555) Pain Care (555) 014-2290</span>
  </div>
  <div class="abs book-btn">Book an Appointment</div>
</div>

<!-- header -->
<div class="abs brand"><div class="brand-mark"></div><div class="brand-name">KOVAR TOTAL RELIEF</div></div>
<nav class="abs nav">
  <a class="active">Home</a><a>About Us</a><a>Pain Procedures</a><a>For Patient</a><a>News</a><a>Testimonials</a><a>Location</a><a>Contact Us</a>
</nav>

<!-- hero -->
<div class="abs hero"></div>
<div class="abs hero-photo" role="img" aria-label="Photo of a physician treating a patient's shoulder"></div>
<div class="abs hero-arrow" style="left:0"><svg width="8" height="12" viewBox="0 0 8 12"><path d="M6 1 1 6l5 5" fill="none" stroke="#fff" stroke-width="2"/></svg></div>
<div class="abs hero-arrow" style="left:821px"><svg width="8" height="12" viewBox="0 0 8 12"><path d="M2 1l5 5-5 5" fill="none" stroke="#fff" stroke-width="2"/></svg></div>
<div class="abs hero-title">Lorem ipsum dolor sit amet adipiscing elit sed diam</div>
<div class="abs hero-btn">Read More »</div>

<!-- service cards -->
<div class="abs card" style="left:30px">
  <div class="abs card-icon" role="img" aria-label="Back pain illustration"></div>
  <h3>Back Pain</h3>
  <p>Lorem ipsum dolor sit amet, consectetuer adipiscing elit, sed diam nonummy nibh</p>
  <div class="bar"></div>
</div>
<div class="abs card" style="left:199px">
  <div class="abs card-icon" role="img" aria-label="Knee pain illustration"></div>
  <h3>Knee Pain</h3>
  <p>Lorem ipsum dolor sit amet, consectetuer adipiscing elit, sed diam nonummy nibh</p>
  <div class="bar"></div>
</div>
<div class="abs card" style="left:368px">
  <div class="abs card-icon" role="img" aria-label="Shoulder pain illustration"></div>
  <h3>Shoulder Pain</h3>
  <p>Lorem ipsum dolor sit amet, consectetuer adipiscing elit, sed diam nonummy nibh</p>
  <div class="bar"></div>
</div>

<!-- schedule form -->
<div class="abs schedule">
  <div class="schedule-head">Schedule an Appointment</div>
  <div class="schedule-intro">Lorem ipsum dolor sit amet, consectetuer adipiscing elit</div>
  <div class="field">First Name</div>
  <div class="field">Email</div>
  <div class="field">Phone</div>
  <div class="field msg">Message</div>
  <div class="captcha-note">Please type the number below</div>
  <div class="captcha-row">
    <div class="captcha-code">1238</div>
    <div class="captcha-input"></div>
    <div class="submit">SUBMIT</div>
  </div>
</div>

<!-- welcome -->
<section class="abs welcome">
  <h2>Welcome To <em>Kovar Total Relief</em></h2>
  <p>Lorem ipsum dolor sit amet, consectetuer adipiscing elit, sed diam nonummy nibh euismod tincidunt ut laoreet dolore magna aliquam erat volutpat. Ut wisi enim ad minim veniam, quis nostrud exerci tation ullamcorper suscipit lobortis nisl ut aliquip ex ea commodo consequat. Duis autem vel eum iriure dolor in hendrerit in vulputate velit esse molestie consequat, vel illum dolore eu feugiat nulla facilisis at vero eros et accumsan et iusto odio dignissim qui blandit praesent luptatum zzril delenit augue duis dolore te feugait nulla facilisi. Lorem ipsum dolor sit amet, consectetuer adipiscing elit, sed diam nonummy nibh euismod tincidunt ut laoreet dolore magna aliquam erat volutpat wisi enim.</p>
  <span class="more">Read More »</span>
</section>
<div class="abs doctor-photo" role="img" aria-label="Portrait of the physician"></div>
<div class="abs doctor-name">Elan Voss, M.D</div>

<div class="abs rule"></div>

<!-- info columns -->
<div class="abs col" style="left:30px">
  <h4>Specialized <b>in Several Procedures</b></h4>
  <ul class="list">
    <li>Epidural Block</li><li>Facet Block</li><li>Radiofrequency Ablation</li><li>Spinal Cord Stimulation</li><li>Shoulder, Hip And Knee Joint Injections</li>
  </ul>
</div>
<div class="abs col insurance" style="left:295px;width:200px">
  <h4><b>Insurance</b> Questions?</h4>
  <p>We accept several insurance plans and accept out of network benefits. Give our office a call and we will help you determine if your eligible to be seen.</p>
  <span class="more">Read More »</span>
</div>
<div class="abs col" style="left:560px">
  <h4>Some Leading <b>Causes of Pain</b></h4>
  <div class="causes">
    <ul class="list">
      <li>Neck Pain</li><li>Back Pain</li><li>Hip Pain</li><li>Radiating Pain</li><li>Knee Pain</li><li>Shoulder Pain</li><li>Muscle Pain</li><li>Carpal Tunnel</li>
    </ul>
    <ul class="list">
      <li>Arthritis Pain</li><li>Cancer Pain</li><li>Face Pain</li><li>Disc Pain</li><li>Phantom Pain</li><li>Post Surgical</li><li>Shingles Pain</li>
    </ul>
  </div>
</div>

<!-- footer -->
<footer class="abs footer"></footer>
<div class="abs fcol" style="left:30px">
  <h5>Quick Links</h5>
  <ul class="flinks">
    <li>Home</li><li>About Us</li><li>Pain Procedures</li><li>For Patient</li><li>News</li><li>Testimonials</li><li>Location</li><li>Contact Us</li>
  </ul>
</div>
<div class="abs fcol hours" style="left:205px;width:150px">
  <h5>Office Hours</h5>
  <p>Monday – Friday<br>8:00 AM – 5:00 PM</p>
  <p style="margin-top:8px"><b>Address</b><br>410 Lindell Avenue, Suite 220<br>Harbor Falls, NV 89021</p>
  <p style="margin-top:8px"><b>Phone</b><br>(555) Pain Care (555) 014-2290</p>
</div>
<div class="abs fcol news" style="left:430px;width:190px">
  <h5>Newsletter Sign Up</h5>
  <p>Sign up for our newsletter to get all the news about our pain practice</p>
  <div class="input">Name</div>
  <div class="input">Email Address</div>
  <div class="go">Submit</div>
</div>
<div class="abs fbrand"><div class="brand-mark"></div><div class="brand-name">KOVAR TOTAL RELIEF</div></div>
<div class="abs copyright">Copyright © 2015 Kovar Total Relief. All Rights Reserved.</div>

</body>
</html>
```